Fresh & clean business card for yacht detailing company
Gullrock detailing
Professional
Captain Morgan tellaver
President
PO box 827 Speonk, ny 11846
Morgan@Gullrockdetailing.com
Gullrockdetailing.com
mtellaver mtellaver
pixelharborworks: #271 - i really like this design, can you add a touch of silver/gray to it?
quillmotionlab: #140 - i really like the back with the logo splitting the blue on bottom & black on top. #142 - i really like the front with the logo in the color at the bottom. can you take the back of #140, put it with the front of #142. Id like to see the color at the bottom in blue and another draft in black?
#34 - maybe a slightly larger logo on front of card?

```html
<!DOCTYPE html>
<html lang="en">
<head>
<meta charset="utf-8">
<title>Gullrock Detailing – Business Card</title>
<link href="https://fonts.googleapis.com/css2?family=Open+Sans:ital,wght@0,400;0,600;1,400&display=swap" rel="stylesheet">
<style>
  :root {
    --backdrop: #e6e6e7;
    --card: #ffffff;
    --ink: #121212;
    --navy: #1c2a5e;
    --royal: #2a4aa8;
    --grey: #5f6166;
    --white: #ffffff;
  }
  html, body {
    margin: 0;
    width: 1200px;
    height: 951px;
    overflow: hidden;
    background: var(--backdrop);
  }
  .stage {
    position: relative;
    width: 1200px;
    height: 951px;
  }
  .card {
    position: absolute;
    left: 220px;
    width: 760px;
    height: 434px;
    border-radius: 26px;
    background: var(--card);
    overflow: hidden;
    box-shadow: 0 6px 18px rgba(0,0,0,0.12);
  }
  .card--front { top: 30px; }
  .card--back { top: 487px; }

  .brand {
    position: absolute;
    font-family: "Open Sans", sans-serif;
  }
  .brand__name {
    margin: 0;
    display: flex;
    align-items: center;
    gap: 12px;
    font-weight: 600;
    color: var(--navy);
    line-height: 1.1;
    white-space: nowrap;
  }
  .brand__mark {
    flex: none;
    border-radius: 50%;
    background: var(--royal);
  }
  .brand__tagline {
    margin: 8px 0 0;
    font-weight: 400;
    color: var(--grey);
    white-space: nowrap;
  }

  .card--front .brand {
    left: 50%;
    top: 50%;
    transform: translate(-50%, -50%);
  }
  .card--front .brand__name { font-size: 40px; }
  .card--front .brand__mark { width: 18px; height: 18px; }
  .card--front .brand__tagline { font-size: 16px; padding-left: 30px; }

  .card--back .divide {
    position: absolute;
    inset: 0;
  }
  .card--back .brand {
    left: 410px;
    top: 150px;
  }
  .card--back .brand__name { font-size: 27px; gap: 10px; }
  .card--back .brand__mark { width: 13px; height: 13px; }
  .card--back .brand__tagline { font-size: 12px; padding-left: 23px; }

  .contact {
    position: absolute;
    left: 34px;
    top: 226px;
    margin: 0;
    padding: 0;
    list-style: none;
    font-family: "Open Sans", sans-serif;
    font-size: 12px;
    color: var(--white);
  }
  .contact li {
    display: flex;
    align-items: center;
    gap: 9px;
    height: 19px;
    white-space: nowrap;
  }
  .contact svg { flex: none; }

  .person {
    position: absolute;
    left: 560px;
    top: 320px;
    font-family: "Open Sans", sans-serif;
  }
  .person__name {
    margin: 0;
    font-size: 19px;
    font-style: italic;
    color: var(--navy);
  }
  .person__role {
    margin: 2px 0 0;
    font-size: 14px;
    font-style: italic;
    color: var(--grey);
  }
</style>
</head>
<body>
<main class="stage">

  <section class="card card--front" aria-label="Card front">
    <div class="brand">
      <p class="brand__name"><span class="brand__mark"></span>Gullrock Detailing</p>
      <p class="brand__tagline">Professional Hull Care &amp; Marine Upkeep</p>
    </div>
  </section>

  <section class="card card--back" aria-label="Card back">
    <svg class="divide" width="760" height="434" viewBox="0 0 760 434" aria-hidden="true">
      <path d="M0,130 C130,95 270,95 325,150 C370,200 340,320 360,434 L0,434 Z" fill="var(--ink)"/>
      <path d="M0,118 C130,83 280,83 337,140 C384,192 354,320 374,434" fill="none" stroke="var(--royal)" stroke-width="8"/>
    </svg>

    <ul class="contact">
      <li><svg width="11" height="11" viewBox="0 0 12 12"><circle cx="6" cy="6" r="6" fill="#fff"/><path d="M6 2.5a2.3 2.3 0 0 0-2.3 2.3C3.7 6.6 6 9.5 6 9.5s2.3-2.9 2.3-4.7A2.3 2.3 0 0 0 6 2.5z" fill="#121212"/></svg>PO Box 827, Speonk</li>
      <li><svg width="11" height="11" viewBox="0 0 12 12"><circle cx="6" cy="6" r="6" fill="#fff"/></svg>NY 11846</li>
      <li><svg width="11" height="11" viewBox="0 0 12 12"><circle cx="6" cy="6" r="6" fill="#fff"/><path d="M4 3l1.2 1.6-.7.8a4 4 0 0 0 2 2l.8-.7L9 8l-.8 1C6 9 3 6 3 3.8z" fill="#121212"/></svg>631 555 0148</li>
      <li><svg width="11" height="11" viewBox="0 0 12 12"><circle cx="6" cy="6" r="6" fill="#fff"/><path d="M4 3l1.2 1.6-.7.8a4 4 0 0 0 2 2l.8-.7L9 8l-.8 1C6 9 3 6 3 3.8z" fill="#121212"/></svg>631 555 0192</li>
      <li><svg width="11" height="11" viewBox="0 0 12 12"><circle cx="6" cy="6" r="6" fill="#fff"/><rect x="3" y="4" width="6" height="4.2" fill="#121212"/></svg>Morgan@Gullrockdetailing.com</li>
      <li><svg width="11" height="11" viewBox="0 0 12 12"><circle cx="6" cy="6" r="6" fill="#fff"/><circle cx="6" cy="6" r="3" fill="none" stroke="#121212" stroke-width="1"/></svg>www.Gullrockdetailing.com</li>
    </ul>

    <div class="brand">
      <p class="brand__name"><span class="brand__mark"></span>Gullrock Detailing</p>
      <p class="brand__tagline">Professional Hull Care &amp; Marine Upkeep</p>
    </div>

    <div class="person">
      <p class="person__name">Morgan Tellaver</p>
      <p class="person__role">Owner / C.E.O.</p>
    </div>
  </section>

</main>
</body>
</html>
```